Marlowe Holdings LLC - Business Cards

Need the following information on the cards:

Name: Dean R Vossler
Title: Chief Executive Manager

Business address:
412 N Ridgeview Lane #118
Carol Stream, Il 60412

Phone: (630) 555-0148 - Business
KPV FFL license number: 5-21-xxx-xx-xx-04519
Email: dean.vossler@marloweholdingsffl.com

Target Market(s)

Firearm owners

Industry/Entity Type

Firearms industry,

Contact Information for Business Card

Contact number, name and title, web page address, email, business address and kpv license number,

Requirements
Must have
• Name, title, business address, phone numbers, KPV license numbers, web page address and email address.
Nice to have
• Cellphone number,

```html
<!DOCTYPE html>
<html lang="en">
<head>
<meta charset="utf-8">
<title>Marlowe Holdings LLC – Business Cards</title>
<link href="https://fonts.googleapis.com/css2?family=Saira+Semi+Condensed:wght@300;400;600&display=swap" rel="stylesheet">
<style>
  :root {
    --bg: #dcdddc;
    --card: #ffffff;
    --red: #cc1f24;
    --grey-strip: #c4c4c4;
    --ink: #2b2b2b;
    --muted: #6b6b6b;
    --white: #ffffff;
  }
  * { margin: 0; padding: 0; box-sizing: border-box; }
  html, body { width: 1200px; height: 1200px; overflow: hidden; }
  body {
    background: var(--bg);
    font-family: "Saira Semi Condensed", sans-serif;
    position: relative;
  }
  .card {
    position: absolute;
    left: 307px;
    width: 539px;
    height: 312px;
    background: var(--card);
    border-radius: 13px;
    overflow: hidden;
  }
  .card--front { top: 188px; }
  .card--back { top: 653px; }

  .brand-name {
    position: absolute;
    color: var(--red);
    font-weight: 600;
    text-align: center;
    text-transform: uppercase;
    line-height: 1.1;
  }
  .card--front .brand-name {
    left: 0; right: 0; top: 124px;
    font-size: 30px;
    letter-spacing: 1px;
  }
  .card--back .brand-name {
    left: 395px; width: 136px; top: 52px;
    font-size: 16px;
    letter-spacing: 0.5px;
  }

  .band { position: absolute; left: 0; top: 0; width: 539px; height: 312px; }

  .person { position: absolute; left: 30px; top: 34px; }
  .person__icon { position: absolute; left: 0; top: 4px; }
  .person__name {
    position: absolute; left: 28px; top: 0;
    font-size: 22px; font-weight: 400; color: var(--ink);
    white-space: nowrap; line-height: 28px;
    padding-right: 10px;
    border-bottom: 1.5px solid var(--red);
  }
  .person__name .first { color: var(--red); font-weight: 600; }
  .person__title {
    position: absolute; left: 28px; top: 34px;
    font-size: 15px; font-weight: 300; color: var(--muted);
    white-space: nowrap;
  }

  .contacts { position: absolute; left: 30px; top: 136px; list-style: none; }
  .contacts li {
    display: flex; align-items: center;
    height: 31px;
    color: var(--white);
    font-size: 17px; font-weight: 300;
    white-space: nowrap;
    letter-spacing: 0.3px;
  }
  .contacts .icon {
    width: 21px; height: 21px; border-radius: 50%;
    background: var(--white);
    display: flex; align-items: center; justify-content: center;
    margin-right: 13px; flex: none;
  }

  .license {
    position: absolute; left: 0; right: 0; top: 260px;
    display: flex; align-items: center; justify-content: center; gap: 12px;
    color: var(--white); font-size: 17px; font-weight: 600;
    white-space: nowrap;
  }
  .license .rule { width: 26px; height: 3px; }
</style>
</head>
<body>

<section class="card card--front" aria-label="Card front">
  <div class="brand-name">Marlowe<br>Holdings LLC</div>
</section>

<section class="card card--back" aria-label="Card back">
  <svg class="band" viewBox="0 0 539 312" aria-hidden="true">
    <path d="M0 96 H262 C300 96 305 104 325 128 C340 146 348 148 380 148 H539 V312 H0 Z" fill="var(--grey-strip)"/>
    <path d="M0 102 H262 C298 102 303 110 322 134 C338 152 346 154 380 154 H539 V312 H0 Z" fill="var(--red)"/>
  </svg>

  <div class="brand-name">Marlowe<br>Holdings LLC</div>

  <div class="person">
    <svg class="person__icon" width="21" height="21" viewBox="0 0 21 21" aria-hidden="true">
      <circle cx="10.5" cy="10.5" r="10.5" fill="var(--red)"/>
      <circle cx="10.5" cy="7.5" r="3" fill="#fff"/>
      <path d="M5.5 16 a5 4.5 0 0 1 10 0 Z" fill="#fff"/>
    </svg>
    <div class="person__name"><span class="first">Dean</span> R Vossler</div>
    <div class="person__title">Chief Executive Manager</div>
  </div>

  <ul class="contacts">
    <li><span class="icon"><svg width="11" height="11" viewBox="0 0 24 24"><path d="M6.6 10.8a15 15 0 0 0 6.6 6.6l2.2-2.2c.3-.3.7-.4 1-.2 1.1.4 2.3.6 3.6.6.6 0 1 .4 1 1V20c0 .6-.4 1-1 1C10.6 21 3 13.4 3 4c0-.6.4-1 1-1h3.5c.6 0 1 .4 1 1 0 1.3.2 2.5.6 3.6.1.3 0 .7-.2 1z" fill="var(--red)"/></svg></span>(630) 555-0148</li>
    <li><span class="icon"><svg width="11" height="9" viewBox="0 0 22 16"><rect x="1" y="1" width="20" height="14" rx="1.5" fill="var(--red)"/><path d="M1.5 2 L11 9 L20.5 2" stroke="#fff" stroke-width="1.6" fill="none"/></svg></span>dean.vossler@marloweholdingsffl.com</li>
    <li><span class="icon"><svg width="12" height="12" viewBox="0 0 24 24" fill="none" stroke="var(--red)" stroke-width="2"><circle cx="12" cy="12" r="10"/><ellipse cx="12" cy="12" rx="4.5" ry="10"/><path d="M2 12h20M4 7h16M4 17h16"/></svg></span>marloweholdingsffl.com</li>
    <li><span class="icon"><svg width="11" height="12" viewBox="0 0 24 26"><path d="M12 1a8 8 0 0 0-8 8c0 6 8 13 8 13s8-7 8-13a8 8 0 0 0-8-8z" fill="none" stroke="var(--red)" stroke-width="2.4"/><circle cx="12" cy="9" r="3" fill="var(--red)"/><path d="M3 25h18" stroke="var(--red)" stroke-width="2"/></svg></span>412 N Ridgeview Lane #118 Carol Stream, Il 60412</li>
  </ul>

  <div class="license">
    <svg class="rule" viewBox="0 0 26 3" aria-hidden="true"><path d="M0 1.5 L26 0 V3 Z" fill="#fff"/></svg>
    <span>KPV FFL license number: 5-21-xxx-xx-xx-04519</span>
    <svg class="rule" viewBox="0 0 26 3" aria-hidden="true"><path d="M26 1.5 L0 0 V3 Z" fill="#fff"/></svg>
  </div>
</section>

</body>
</html>
```